Velorin dog shampoos

We need new labels for an already existing line of dog shampoos; this is our classic VELORIN range; Here is our website www.laboratoire-velorin-example.be.We attach a photo of 2 vials which should both have the new labels and some photos of the already existing vials.
Our customers are both individuals and professionals.
We would like to keep the identity of the product while modernizing it.
We also attach the logo.
the label must be partially or fully transparent; Customers often identify products with the color of the liquid.
taking the example of the ALOE VERA shampoo, we would like the specificities to be more visible than currently, possibly with a font larger than the name ALOE VERA;
there must be room for the text in both English and French;
Here is the text for the forehead: Moisturizing and regenerating shampoo.
The paw on the current label may disappear, however, it is necessary that there is a recall related to the dogs.
Here are a few examples of what we love
Thank you

Target Market(s)

INDIVIDUALS AND PROFESSIONALS

Industry/Entity Type

COSMETIQUES CHIENS

Requirements
Must have
• eed new labels for an already existing line of dog shampoos; this is our classic VELORIN range; Here is our website www.laboratoire-velorin-example.be.We attach a photo of 2 vials which should both have the new labels and some photos of the already existing vials. Our customers are both individuals and professionals. We would like to keep the identity of the product while modernizing it. We also attach the logo. the label must be partially or fully transparent; Customers often identify products with the color of the liquid. taking the example of the ALOE VERA shampoo, we would like the specificities to be more visible than currently, possibly with a font larger than the name ALOE VERA; there must be room for the text in both English and French; Here is the text for the forehead: Moisturizing and regenerating shampoo. The paw on the current label may disappear, however, it is necessary that there is a recall related to the dogs. Here are a few examples of what we love
Nice to have
• same lay out for each product;
Should not have
• humorous dog

```html
<!DOCTYPE html>
<html lang="fr">
<head>
<meta charset="utf-8">
<title>Velorin — Shampooing Aloe Vera</title>
<link rel="stylesheet" href="https://fonts.googleapis.com/css2?family=Poppins:wght@300;400;700;800&family=Vollkorn:ital,wght@1,700&display=swap">
<style>
  :root {
    --backdrop: #d9e8a6;
    --label-white: #ffffff;
    --ink: #111111;
    --leaf-green: #6cb42c;
    --leaf-deep: #3f8a1f;
    --leaf-light: #a8d46a;
    --mark-tone: #b9cf82;
  }
  * { margin: 0; padding: 0; box-sizing: border-box; }
  html, body { width: 1200px; height: 946px; overflow: hidden; }
  body {
    background: var(--backdrop);
    font-family: "Poppins", sans-serif;
    position: relative;
  }
  .brand {
    position: absolute;
    left: 475px; top: 66px; width: 234px;
    color: var(--ink);
    font-family: "Poppins", sans-serif;
    font-weight: 800;
    text-align: center;
    line-height: 1;
  }
  .brand-lab { font-size: 22px; letter-spacing: 2px; display: block; }
  .brand-name { font-size: 40px; letter-spacing: 2px; display: block; margin-top: 2px; }

  .aloe-plants {
    position: absolute;
    left: 283px; top: 262px; width: 634px; height: 380px;
    border-radius: 50% 50% 30% 30% / 70% 70% 30% 30%;
    background: radial-gradient(ellipse at 50% 80%, var(--leaf-deep) 0%, var(--leaf-green) 45%, rgba(168,212,106,0) 72%);
  }

  .label {
    position: absolute;
    left: 464px; top: 211px; width: 254px; height: 482px;
    background: var(--label-white);
    padding: 8px;
  }
  .label-frame {
    position: relative;
    width: 100%; height: 100%;
    border: 1.5px solid var(--ink);
    text-align: center;
  }
  .title-fr {
    position: absolute; left: 0; right: 0; top: 22px;
    font-weight: 700; font-size: 31px; letter-spacing: -0.3px;
    color: var(--leaf-green); line-height: 1;
  }
  .sub-fr {
    position: absolute; left: 0; right: 0; top: 58px;
    font-weight: 300; font-size: 19px; line-height: 22px;
    color: var(--leaf-green);
  }
  .title-en {
    position: absolute; left: 0; right: 0; top: 117px;
    font-weight: 800; font-size: 21px; color: var(--ink); line-height: 1;
  }
  .sub-en {
    position: absolute; left: 0; right: 0; top: 144px;
    font-weight: 400; font-size: 12.5px; line-height: 16px; color: var(--ink);
  }
  .aloe-leaf {
    position: absolute; left: 14px; top: 170px; width: 220px; height: 150px;
    background: linear-gradient(160deg, rgba(255,255,255,0) 30%, var(--leaf-light) 55%, var(--leaf-deep) 85%);
    border-radius: 80% 10% 60% 30% / 70% 20% 60% 40%;
  }
  .extract-line {
    position: absolute; left: 0; right: 0; top: 348px;
    font-family: "Vollkorn", serif; font-style: italic; font-weight: 700;
    font-size: 18px; color: var(--ink);
  }
  .extract-name {
    position: absolute; left: 0; right: 0; top: 370px;
    font-family: "Vollkorn", serif; font-style: italic; font-weight: 700;
    font-size: 38px; line-height: 36px; color: var(--leaf-green);
  }

  .dog-mark {
    position: absolute;
    left: 483px; top: 735px; width: 226px; height: 178px;
    border-radius: 45%;
    background: radial-gradient(ellipse at center, var(--mark-tone) 0%, rgba(185,207,130,0) 70%);
  }
</style>
</head>
<body>
  <div class="brand">
    <span class="brand-lab">Laboratoire</span>
    <span class="brand-name">VELORIN</span>
  </div>

  <div class="aloe-plants" role="img" aria-label="Photographie de plantes d'aloe vera derrière l'étiquette"></div>

  <div class="label">
    <div class="label-frame">
      <p class="title-fr">SHAMPOOING</p>
      <p class="sub-fr">HYDRATANT ET<br>RÉGÉNÉRANT</p>
      <p class="title-en">SHAMPOO</p>
      <p class="sub-en">MOISTURISING &amp;<br>REGENERATING<br>SHAMPOO</p>
      <div class="aloe-leaf" role="img" aria-label="Photographie d'une feuille d'aloe vera avec gouttes d'eau"></div>
      <p class="extract-line">à l’extrait</p>
      <p class="extract-name">d’Aloe Vera<br>BIO</p>
    </div>
  </div>

  <div class="dog-mark" role="img" aria-label="Illustration au trait d'un chien entouré de bulles de savon"></div>
</body>
</html>
```